Need bath soak label done. READ BRIEF. Brand is Auntie sings softly. Will attach file for copying.

We want the attached file copied with editable files please. it was generated with AI so the words dont make sense but things to replace lines with are things like "cooling vapors" "the best bath ever" "bath soak" "lemon" "eucalyptus" "all natural"...things like that. BUT MAKE SURE TO COPY IT EXACTLY. IF YOU DO I WILL TIP 500. I like the purple one by the way. if you can include a version or two that includes an image of a claw foot tub, you would be even better!!!! possibly...would just like to see it. make sure you recreate this EXACTLY PLEASE. Do not change it. ADD CLAWFOOT TUB PLS IN MIDDLE

Target Market(s)

women and people that take baths...not just babies

Requirements
Must have
• what i mentioned in the brief...i attached the exact thing i need you to recreate.
Nice to have
• maybe try a clawfoot tub but that is a secondary design not the one i need that i may like

```html
<!DOCTYPE html>
<html lang="en">
<head>
<meta charset="utf-8">
<title>Auntie Sings Softly – Bath Soak Label</title>
<link rel="stylesheet" href="https://fonts.googleapis.com/css2?family=Abril+Fatface&family=Oswald:wght@400;500&family=Poppins:wght@600&display=swap">
<style>
  :root {
    --page: #ffffff;
    --pouch-edge: #cdc3d6;
    --pouch-top: #ddd4e3;
    --label: #ece0e1;
    --label-glow: #f5ece9;
    --mint: #cfe8e0;
    --mint-deep: #9cc9bb;
    --leaf: #8dbcae;
    --navy: #1b2747;
    --navy-soft: #2e3c5e;
    --cloud: #f8f3f1;
    --frame: #9f97ad;
  }
  * { box-sizing: border-box; margin: 0; padding: 0; }
  html, body { width: 1200px; height: 1200px; overflow: hidden; background: var(--page); }

  .canvas { position: relative; width: 1200px; height: 1200px; background: var(--page); }

  .label {
    position: absolute; left: 234px; top: 48px; width: 702px; height: 1086px;
    background: var(--pouch-edge);
    border-radius: 6px;
  }
  .label__top-band {
    position: absolute; left: 0; top: 0; width: 100%; height: 108px;
    background: var(--pouch-top);
    border-bottom: 2px solid var(--frame);
  }
  .label__panel {
    position: absolute; left: 18px; top: 132px; width: 666px; height: 930px;
    background:
      linear-gradient(180deg, rgba(207,232,224,.85) 0%, rgba(207,232,224,0) 14%),
      radial-gradient(ellipse at 50% 42%, var(--label-glow) 0%, var(--label) 60%, #e4d6dc 100%);
    border: 2px solid var(--frame);
    outline: 1px solid var(--frame);
    outline-offset: 6px;
  }

  .ornament { position: absolute; }
  .ornament--vine-left,
  .ornament--vine-right {
    top: 156px; width: 90px; height: 400px;
    background: radial-gradient(ellipse at 50% 45%, rgba(141,188,174,.5) 0%, rgba(141,188,174,.2) 45%, rgba(141,188,174,0) 72%);
  }
  .ornament--vine-left { left: 36px; }
  .ornament--vine-right { left: 576px; }

  .ornament--sprig-left,
  .ornament--sprig-right {
    top: 820px; width: 150px; height: 220px;
    background: radial-gradient(ellipse at 50% 55%, rgba(141,188,174,.55) 0%, rgba(141,188,174,.22) 45%, rgba(141,188,174,0) 72%);
  }
  .ornament--sprig-left { left: 52px; }
  .ornament--sprig-right { left: 500px; }

  .ornament--clouds {
    left: 90px; width: 522px; top: 300px; height: 110px;
    background: radial-gradient(ellipse at 50% 60%, var(--cloud) 0%, rgba(248,243,241,0) 70%);
  }
  .ornament--crest {
    left: 296px; top: 282px; width: 110px; height: 36px;
    background: radial-gradient(ellipse, #f3f0ee 0%, #d9d2d8 65%, rgba(217,210,216,0) 100%);
  }
  .ornament--swirl {
    left: 170px; width: 362px; top: 640px; height: 50px;
    background: radial-gradient(ellipse, rgba(46,60,94,.12) 0%, rgba(46,60,94,0) 70%);
  }

  .ribbon { position: absolute; }
  .ribbon--tag { left: 96px; top: 190px; width: 510px; height: 90px; }
  .ribbon--name { left: 174px; top: 696px; width: 354px; height: 82px; }

  .tagline {
    position: absolute; left: 0; width: 100%; text-align: center;
    font-family: 'Poppins', sans-serif; font-weight: 600;
    font-size: 40px; line-height: 1; letter-spacing: 1px; color: var(--navy);
    top: 214px;
  }
  .brand {
    position: absolute; left: 0; width: 100%; text-align: center;
    font-family: 'Abril Fatface', serif; color: var(--navy); line-height: 1;
    text-shadow: 3px 3px 0 rgba(255,255,255,.6);
  }
  .brand__line1 { top: 366px; font-size: 132px; letter-spacing: 2px; }
  .brand__line2 { top: 560px; font-size: 70px; letter-spacing: 1px; }

  .product {
    position: absolute; left: 0; width: 100%; text-align: center;
    font-family: 'Oswald', sans-serif; color: var(--navy); line-height: 1;
  }
  .product__name { top: 714px; font-size: 48px; font-weight: 500; letter-spacing: 3px; }
  .product__claim { top: 784px; font-size: 30px; font-weight: 400; letter-spacing: 1.5px; }
  .product__tub { position: absolute; left: 311px; top: 848px; width: 80px; height: 44px; }
  .product__scent { top: 904px; font-size: 28px; font-weight: 400; letter-spacing: 1.5px; }
  .product__natural { top: 940px; font-size: 28px; font-weight: 400; letter-spacing: 1.5px; }
</style>
</head>
<body>
<main class="canvas">
  <section class="label">
    <div class="label__top-band"></div>
    <div class="label__panel"></div>

    <div class="ornament ornament--vine-left" role="img" aria-label="Leafy vine decoration on the left side"></div>
    <div class="ornament ornament--vine-right" role="img" aria-label="Leafy vine decoration on the right side"></div>
    <div class="ornament ornament--clouds" role="img" aria-label="Soft steam clouds behind the brand name"></div>
    <div class="ornament ornament--crest" role="img" aria-label="Small winged crest ornament"></div>
    <div class="ornament ornament--swirl" role="img" aria-label="Flourish swirl ornament"></div>
    <div class="ornament ornament--sprig-left" role="img" aria-label="Leaf sprig decoration, lower left"></div>
    <div class="ornament ornament--sprig-right" role="img" aria-label="Leaf sprig decoration, lower right"></div>

    <svg class="ribbon ribbon--tag" viewBox="0 0 510 90" aria-hidden="true">
      <path d="M0 30 L44 22 L44 78 L0 86 L20 58 Z" fill="var(--mint-deep)"/>
      <path d="M510 30 L466 22 L466 78 L510 86 L490 58 Z" fill="var(--mint-deep)"/>
      <path d="M32 14 Q255 -6 478 14 L478 72 Q255 54 32 72 Z" fill="var(--mint)" stroke="var(--navy-soft)" stroke-width="1.5"/>
    </svg>
    <p class="tagline">COOLING VAPORS</p>

    <h1 class="brand brand__line1">AUNTIE</h1>
    <h2 class="brand brand__line2">SINGS SOFTLY</h2>

    <svg class="ribbon ribbon--name" viewBox="0 0 354 82" aria-hidden="true">
      <path d="M10 8 Q177 -2 344 8 L340 68 Q177 58 14 68 Z" fill="#f3ebe8" stroke="var(--navy-soft)" stroke-width="1.5"/>
      <path d="M14 68 Q4 76 18 80 L40 72" fill="none" stroke="var(--navy-soft)" stroke-width="1.5"/>
      <path d="M340 68 Q350 76 336 80 L314 72" fill="none" stroke="var(--navy-soft)" stroke-width="1.5"/>
    </svg>
    <p class="product product__name">BATH SOAK</p>
    <p class="product product__claim">THE BEST BATH EVER</p>

    <svg class="product__tub" viewBox="0 0 80 44" aria-hidden="true">
      <line x1="0" y1="22" x2="80" y2="22" stroke="var(--navy)" stroke-width="2"/>
      <path d="M12 22 L68 22 L64 34 Q40 38 16 34 Z" fill="var(--navy)"/>
      <path d="M14 22 L14 8 Q14 4 20 4" fill="none" stroke="var(--navy)" stroke-width="2"/>
      <line x1="20" y1="34" x2="18" y2="40" stroke="var(--navy)" stroke-width="2"/>
      <line x1="60" y1="34" x2="62" y2="40" stroke="var(--navy)" stroke-width="2"/>
      <circle cx="52" cy="12" r="2.5" fill="var(--navy)"/>
      <circle cx="60" cy="6" r="2" fill="var(--navy)"/>
    </svg>

    <p class="product product__scent">LEMON · EUCALYPTUS</p>
    <p class="product product__natural">ALL NATURAL</p>
  </section>
</main>
</body>
</html>
```